Brightwell Mechanical - Business Card Design

We would like a dark (likely black) themed business card to be able to hand out to potential clients. We may list our services on the card or keep it clean. Unsure. Logo attached

```html
<!DOCTYPE html>
<html lang="en">
<head>
<meta charset="utf-8">
<title>Brightwell Mechanical – Business Card</title>
<link href="https://fonts.googleapis.com/css2?family=Montserrat:wght@500;600;800&display=swap" rel="stylesheet">
<style>
  :root{
    --stage:#2c2c2e;
    --card:#121a26;
    --card-deep:#0b111a;
    --blue:#2f7fd0;
    --orange:#ee5a24;
    --ink:#f1f3f6;
    --pattern-a:#1a2738;
    --pattern-b:#3a2420;
  }
  *{box-sizing:border-box;margin:0;padding:0}
  html,body{width:1200px;height:900px;overflow:hidden}
  body{background:var(--stage);font-family:"Montserrat",sans-serif;position:relative}

  .card{position:absolute;width:640px;height:366px;border-radius:18px;overflow:hidden;
        background:linear-gradient(135deg,var(--card) 0%,var(--card-deep) 100%);
        box-shadow:0 18px 40px rgba(0,0,0,.45)}

  /* back side */
  .card--back{left:70px;top:50px}
  .back-pattern{position:absolute;inset:0;
        background:radial-gradient(circle at 30% 40%,var(--pattern-a) 0%,transparent 60%),
                   radial-gradient(circle at 70% 65%,var(--pattern-b) 0%,transparent 65%),
                   var(--card-deep)}
  .back-brand{position:absolute;right:34px;top:150px;display:flex;align-items:center;gap:10px;
        color:var(--ink);font-weight:800;font-size:18px;letter-spacing:.04em;text-transform:uppercase}
  .dot{display:inline-block;border-radius:50%;background:var(--orange);flex:none}
  .back-brand .dot{width:22px;height:22px}

  /* front side */
  .card--front{left:490px;top:480px}
  .edge-accent{position:absolute;left:0;top:150px;width:8px;height:70px;background:var(--orange)}
  .front-glow{position:absolute;right:-60px;top:-40px;width:300px;height:300px;border-radius:50%;
        background:radial-gradient(circle,rgba(60,40,40,.55) 0%,transparent 70%)}

  .brand{position:absolute;left:36px;top:40px;display:flex;align-items:center;gap:14px}
  .brand .dot{width:46px;height:46px}
  .brand-name{color:var(--blue);font-weight:800;font-size:30px;line-height:1;letter-spacing:.02em;text-transform:uppercase}

  .person{position:absolute;left:44px;top:130px}
  .person-name{color:var(--blue);font-weight:600;font-size:24px}
  .person-role{color:var(--orange);font-weight:500;font-size:14px;margin-top:2px}

  .address{position:absolute;left:44px;top:196px;font-size:13px;line-height:1.4;color:var(--ink);font-weight:500}
  .address .company{color:var(--orange)}

  .contacts{position:absolute;left:44px;top:266px;list-style:none;font-size:13px;color:var(--ink);font-weight:500}
  .contacts li{display:flex;align-items:center;gap:10px;height:24px}
  .contacts svg{width:14px;height:14px;fill:var(--orange);flex:none}
  .contacts .accent{color:var(--orange)}

  .services{position:absolute;right:34px;top:120px;list-style:none;text-align:right;font-size:13px;color:var(--ink);font-weight:500}
  .services li{display:flex;align-items:center;justify-content:flex-end;gap:10px;height:24px}
  .services .dot{width:11px;height:11px;background:none;border:2px solid var(--orange)}
</style>
</head>
<body>

<section class="card card--back" aria-label="Business card back">
  <div class="back-pattern" role="img" aria-label="Repeating company emblem pattern in dark blue and rust tones"></div>
  <div class="back-brand"><span class="dot"></span>Brightwell Mechanical</div>
</section>

<section class="card card--front" aria-label="Business card front">
  <div class="front-glow" role="img" aria-label="Faint large company emblem decoration"></div>
  <div class="edge-accent"></div>

  <div class="brand"><span class="dot"></span><span class="brand-name">Brightwell Mechanical Inc</span></div>

  <div class="person">
    <p class="person-name">Daniel Reyes</p>
    <p class="person-role">Managing Director</p>
  </div>

  <p class="address"><span class="company">Brightwell Mechanical Inc,</span><br>Here is your address<br>Road No, 123, United States</p>

  <ul class="contacts">
    <li><svg viewBox="0 0 16 16"><path d="M3 1h3l1 4-2 1a9 9 0 0 0 5 5l1-2 4 1v3c0 1-1 2-2 2A13 13 0 0 1 1 3c0-1 1-2 2-2z"/></svg>5550142277</li>
    <li><svg viewBox="0 0 16 16"><path d="M1 3h14v10H1z M1 3l7 6 7-6" fill="none" stroke="#ee5a24" stroke-width="1.6"/></svg>hello@brightwellmech.com</li>
    <li><svg viewBox="0 0 16 16"><circle cx="8" cy="8" r="6.5" fill="none" stroke="#ee5a24" stroke-width="1.5"/><path d="M1.5 8h13M8 1.5c-3 3.5-3 9.5 0 13M8 1.5c3 3.5 3 9.5 0 13" fill="none" stroke="#ee5a24" stroke-width="1.2"/></svg><span>www.<span class="accent">brightwellmech</span>.com</span></li>
  </ul>

  <ul class="services">
    <li>Here is your services<span class="dot"></span></li>
    <li>Here is your services<span class="dot"></span></li>
    <li>Here is your services<span class="dot"></span></li>
    <li>Here is your services<span class="dot"></span></li>
    <li>Here is your services<span class="dot"></span></li>
    <li>Here is your services<span class="dot"></span></li>
  </ul>
</section>

</body>
</html>
```